Healthcare Technology Presentation Folder + Proposal Front Page + Letter Head

We require someone to come up with stationery design theme the following

- Presentation Folders - Template supplied
- Proposal Front Page - A4
- Letter Head - A4

I've provided our company logo, and also the presentation folder template to use.
The Letter head template and Proposal front page design is to be provided in Microsoft Word. Presentation Folder to be provided on the template we have supplied or so long as the dimensions match.

We are looking for a new fresh look, professional design with our target audience being healthcare professionals. Prefer the colour scheme of our logo and traditional black

The presentation folder is to look professional, have our website address tarvelhub.com.au and no other information. Some nice accompanying graphics.

The Letter Head / Proposal Front page must have the following information
- Our logo
- Suite 38, 219 Kendrow Street
Port Melbourne, Victoria, 3184
- Phone: 03 9417 3865
- Fax: 03 9582 4716
- Web: tarvelhub.com.au

The winning design must contain all three designs with a consistent look and feel

Target Market(s)

Healthcare Professional

Font styles to use
Sans Serif

Requirements
Must have
• Our company colours
Should not have
• Healthcare Symbols

```html
<!DOCTYPE html>
<html lang="en">
<head>
<meta charset="utf-8">
<title>Tarvelhub Presentation Folder</title>
<link href="https://fonts.googleapis.com/css2?family=Open+Sans:wght@400;600&display=swap" rel="stylesheet">
<style>
  :root {
    --backdrop: #dcdcdc;
    --folder-black: #2a2827;
    --pattern-blue: #3f78b0;
    --pattern-dark: #2b323b;
    --pattern-mid: #304457;
    --brand-blue: #3d6c99;
    --brand-orange: #f0962e;
  }
  html, body {
    margin: 0;
    padding: 0;
    overflow: hidden;
  }
  .canvas {
    position: relative;
    width: 1200px;
    height: 847px;
    background: var(--backdrop);
    overflow: hidden;
    font-family: "Open Sans", Arial, sans-serif;
  }
  .folder-dieline {
    position: absolute;
    inset: 0;
  }
  .folder-panel { fill: var(--folder-black); }
  .folder-fold { stroke: #222020; stroke-width: 1; }
  .pattern-edge {
    fill: none;
    stroke: var(--pattern-blue);
    stroke-width: 1.2;
    stroke-linejoin: round;
  }
  .brand {
    position: absolute;
    left: 760px;
    top: 168px;
    display: flex;
    align-items: center;
    gap: 10px;
  }
  .brand-mark {
    width: 26px;
    height: 26px;
    border-radius: 50%;
    background: var(--brand-orange);
  }
  .brand-name {
    font-size: 30px;
    font-weight: 600;
    letter-spacing: -0.5px;
    color: var(--brand-blue);
    line-height: 1;
  }
  .brand-web {
    position: absolute;
    left: 846px;
    top: 220px;
    width: 100px;
    text-align: right;
    font-size: 8.5px;
    font-weight: 600;
    color: var(--brand-blue);
    letter-spacing: 0.2px;
  }
</style>
</head>
<body>
<div class="canvas">
  <svg class="folder-dieline" width="1200" height="847" viewBox="0 0 1200 847">
    <defs>
      <linearGradient id="pattern-tone" x1="0" y1="0" x2="0" y2="1">
        <stop offset="0" stop-color="var(--pattern-mid)"/>
        <stop offset="1" stop-color="var(--pattern-dark)"/>
      </linearGradient>
    </defs>

    <!-- side glue flap -->
    <path class="folder-panel" d="M287 226 L268 226 Q232 226 228 270 L165 560 L287 605 Z"/>
    <!-- bottom pocket flap -->
    <path class="folder-panel" d="M287 605 L648 605 L648 710 Q520 735 385 752 L287 605 Z"/>
    <!-- back and front covers -->
    <rect class="folder-panel" x="287" y="96" width="749" height="509"/>
    <line class="folder-fold" x1="666" y1="96" x2="666" y2="605"/>

    <!-- decorative triangle band -->
    <g role="img" aria-label="Band of interlocking blue outline triangles across the lower folder">
      <path fill="url(#pattern-tone)" d="M205 372 L280 345 L287 342 L287 605 L165 560 Z"/>
      <path fill="url(#pattern-tone)" d="M287 410 L308 340 L375 402 L480 380 L470 470 L660 420 L760 390 L830 452 L935 430 L1036 400 L1036 605 L287 605 Z"/>
      <path fill="url(#pattern-tone)" d="M290 612 L648 612 L648 710 Q520 735 385 752 Z"/>
      <path class="pattern-edge" d="M205 372 L280 345"/>
      <path class="pattern-edge" d="M287 410 L308 340 L375 402 L480 380 L470 470 L660 420 L760 390 L830 452 L935 430 L1036 400"/>
    </g>
  </svg>

  <div class="brand">
    <span class="brand-mark"></span>
    <span class="brand-name">tarvelhub</span>
  </div>
  <div class="brand-web">tarvelhub.com.au</div>
</div>
</body>
</html>
```